Letterhead - Pelvarosi Law Group

I receive a fantastic logo from you guys and I'd like to incorporate it into business cards and letterhead. I accidentally approved design No. 58027913 and contacted designer Tarveck, and Tarveck sent me the zip folder for Design No. 58027986, which I very much appreciate.
I'd like to order business cards and letterhead with Design No. 58027986 as soon as possible, but I want to make sure that you incorporate the correct design (attached). I'd also like to provide my information to add (address, phone number, email, fax) but I'm not quite sure how to do it.
The information that I would like on the business cards and letterhead is as follows:
Pelvarosi Law Group
Dorian K. Pelvarosi, Esq.
2741 Halvern Street, Suite 306
San Francisco, CA 94019
Office: (415) 738-0461
Fax: (415) 386-7710
dory@pelvarosilawgroup.com
Thanks in advance for any guidance.
Dory Pelvarosi
Pelvarosi Law Group
(415) 574-8839 (cell)

```html
<!DOCTYPE html>
<html lang="en">
<head>
<meta charset="utf-8">
<title>Pelvarosi Law Group – Letterhead</title>
<link rel="stylesheet" href="https://fonts.googleapis.com/css2?family=Arimo:wght@400;700&family=Mulish:wght@700&display=swap">
<style>
  :root {
    --backdrop: #e2e2e2;
    --paper: #ffffff;
    --ink: #1b1b18;
    --text: #505050;
    --muted: #808080;
    --rule: #8a8a8a;
    --brand-blue: #0a8ccb;
  }
  * { box-sizing: border-box; margin: 0; padding: 0; }
  html, body { width: 1200px; height: 1170px; overflow: hidden; background: var(--backdrop); }
  .letterhead {
    position: absolute; left: 240px; top: 75px; width: 721px; height: 1019px;
    background: var(--paper); box-shadow: 2px 3px 6px rgba(0,0,0,.25); overflow: hidden;
    font-family: "Arimo", Arial, sans-serif; color: var(--text);
  }
  .brand {
    position: absolute; left: 56px; top: 56px; display: flex; align-items: center; gap: 12px;
  }
  .brand-mark { width: 18px; height: 18px; background: var(--brand-blue); flex: none; }
  .brand-name {
    font-family: "Arimo", Arial, sans-serif; font-weight: 700; font-size: 27px; line-height: 31px;
    color: var(--ink); letter-spacing: .5px; text-transform: uppercase;
  }
  .contact {
    position: absolute; left: 481px; top: 49px; font-style: normal;
    font-size: 12.6px; color: var(--muted); line-height: 17.2px;
  }
  .contact-line { display: flex; align-items: center; gap: 6px; }
  .contact-line svg { width: 12px; height: 12px; fill: var(--brand-blue); flex: none; }
  .address { margin-top: 4px; line-height: 14.8px; }
  .header-rule { position: absolute; left: 56px; top: 141px; width: 608px; height: 1px; background: var(--rule); }
  .salutation {
    position: absolute; left: 66px; top: 313px; font-family: "Mulish", sans-serif;
    font-weight: 700; font-size: 16.5px; color: var(--text);
  }
  .body-copy { position: absolute; left: 64px; top: 362px; width: 592px; font-size: 12.4px; line-height: 14.8px; }
  .body-copy p + p { margin-top: 12.5px; }
  .closing {
    position: absolute; left: 66px; top: 666px; font-family: "Mulish", sans-serif;
    font-weight: 700; font-size: 9px; color: var(--text);
  }
  .signature { position: absolute; left: 66px; top: 710px; width: 118px; height: 34px; background: #e6e6e6; }
  .footer-band {
    position: absolute; left: 0; bottom: 0; width: 721px; height: 74px;
    background: linear-gradient(100deg, var(--brand-blue) 0%, var(--ink) 70%);
  }
</style>
</head>
<body>
<main class="letterhead">
  <div class="brand">
    <span class="brand-mark"></span>
    <span class="brand-name">Pelvarosi<br>Law Group</span>
  </div>

  <address class="contact">
    <div class="contact-line">
      <svg viewBox="0 0 24 24" aria-hidden="true"><path d="M6.6 10.8a15.1 15.1 0 0 0 6.6 6.6l2.2-2.2c.3-.3.7-.4 1-.2 1.1.4 2.3.6 3.6.6.6 0 1 .4 1 1V20c0 .6-.4 1-1 1A17 17 0 0 1 3 4c0-.6.4-1 1-1h3.5c.6 0 1 .4 1 1 0 1.3.2 2.5.6 3.6.1.3 0 .7-.2 1z"/></svg>
      <span>(415) 738-0461</span>
    </div>
    <div class="contact-line">
      <svg viewBox="0 0 24 24" aria-hidden="true"><path d="M6 2h12v6H6zM3 9h18v9h-3v4H6v-4H3zm5 6v5h8v-5z"/></svg>
      <span>(415) 386-7710</span>
    </div>
    <div class="contact-line">
      <svg viewBox="0 0 24 24" aria-hidden="true"><path d="M2 5h20v14H2zm2 2v.5l8 5.5 8-5.5V7z"/></svg>
      <span>dory@pelvarosilawgroup.com</span>
    </div>
    <div class="address">2741 Halvern Street, Suite 306<br>San Francisco, CA 94019</div>
  </address>

  <div class="header-rule"></div>

  <h1 class="salutation">Dear Mr. Calloway,</h1>

  <section class="body-copy">
    <p>Lorem ipsum dolor sit amet, consectetuer adipiscing elit, sed diam nonmmy nibh euismod tincidunt ut laor eet dolore magna aliquam erat volutpat. Ut wisi enim ad minim veniam, quis nostrud exerci tationmcorper suscipit lobortis nisl ut aliquip ex ea commodo consequat. Duis autem vel eum iriure dolor in hendrerit in vulputate velit esse molestie consequat, vel illum dolore eu feugiat</p>
    <p>Rorem ipsum dolor sit amet, consectetuer adipiscing elit, sed diam nonmmy nibh euismod tincidunt ut laor eet dolore magna aliquam erat volutpat. Ut wisi enim ad minim veniam, quis nostrud exerci tationmcorper suscipit lobortis nisl ut aliquip ex ea commodo consequat. Duis autem vel eum iriure dolor in hendrerit in vulputate velit esse molest</p>
    <p>Dorem ipsum dolor sit amet, consectetuer adipiscing elit, sed diam nonmmy nibh euismod tincidunt ut laor eet dolore magna aliquam erat volutpat. Ut wisi enim ad minim veniam, quis nostrud exerci tationmcorper suscipit lobortis nisl ut aliquip ex ea commodo consequat. Duis autem vel eum iriure dolor in hendrerit in suscipit lobortis nisl ut aliquip ex ea commodo consequat. Duis autem vel eum iriure dolor in hendrerit in vulputate velit esse molestie consequat, vel illum</p>
    <p>Sorem ipsum dolor sit amet, consectetuer adipiscing elit, sed diam nonmmy nibh euismod tincidunt ut laor eet dolore magna aliquam erat volutpat. Ut wisi enim ad minim veniam, quis nostrud exerci tationmcorper suscipit lobortis nisl ut aliquip ex ea commodo consequat. Duis autem vel eum iriure dolor in</p>
  </section>

  <p class="closing">Sincerely,</p>
  <div class="signature" role="img" aria-label="Handwritten signature of the sender"></div>

  <div class="footer-band" role="img" aria-label="Decorative blue and black footer band"></div>
</main>
</body>
</html>
```